Cosmetic Surgery Ad for a magazine

We would like design options for our cosmetic surgery practice located in California for summer advertizing breast augmentation and liposuction to get ready for a beach body.

Target Market(s)

Women ages 25 - 40

Industry/Entity Type

Cosmetic

Other font styles liked:
• see brand standards attachment

Requirements
Must have
• Our logo (see brand standards attachment)
Should not have
• Nudity

```html
<!DOCTYPE html>
<html lang="en">
<head>
<meta charset="utf-8">
<title>Belleform – Perfect Beach Body</title>
<link rel="stylesheet" href="https://fonts.googleapis.com/css2?family=Arimo:ital,wght@0,400;0,700;1,700&family=Oswald:wght@700&display=swap">
<style>
  :root {
    --sky-top: #6f8b9b;
    --sky-mid: #9fb9c3;
    --sky-low: #cfe4e6;
    --ink: #1b1b1b;
    --ink-soft: #2c3a40;
    --pink: #e9849d;
    --green: #8fc28c;
    --gold: #d9b23c;
    --gold-deep: #b98a1c;
  }
  * { margin: 0; padding: 0; box-sizing: border-box; }
  html, body { width: 893px; height: 1200px; overflow: hidden; }
  body {
    position: relative;
    font-family: "Arimo", Arial, sans-serif;
    color: var(--ink);
    background: linear-gradient(180deg, var(--sky-top) 0%, var(--sky-mid) 55%, var(--sky-low) 100%);
  }
  .abs { position: absolute; }

  /* Brand lockup */
  .brand-name {
    left: 52px; top: 190px;
    font-size: 74px; font-weight: 400; letter-spacing: -1px;
    color: var(--green); line-height: 1;
  }
  .brand-tagline {
    left: 58px; top: 278px;
    font-size: 19px; font-weight: 400; letter-spacing: .5px;
    color: var(--pink); text-transform: uppercase;
  }

  /* Headline */
  .headline {
    left: 72px; top: 340px;
    font-family: "Oswald", Impact, sans-serif;
    font-weight: 700; font-size: 66px; line-height: 1.02;
    color: var(--ink); text-transform: uppercase; letter-spacing: 1px;
  }
  .headline-brace { left: 60px; top: 500px; }

  /* Hero photo area */
  .hero-photo {
    left: 110px; top: 545px; width: 300px; height: 655px;
    background: linear-gradient(180deg, rgba(214,170,130,.0) 0%, rgba(214,170,130,.75) 12%, #d8aa84 42%, #c9936b 66%, #b7657a 82%, #6f8fb0 100%);
    border-radius: 150px 150px 0 0;
  }

  /* Divider arrow */
  .divider-arrow { left: 455px; top: 70px; }

  /* Right column */
  .kicker { left: 520px; top: 150px; line-height: 1.05; }
  .kicker-pink { font-size: 34px; font-weight: 700; color: var(--pink); display: block; }
  .kicker-dark { font-size: 36px; font-weight: 700; color: var(--ink); display: block; }
  .kicker-amp {
    left: 690px; top: 168px;
    font-size: 110px; font-weight: 700; color: var(--green); line-height: 1;
  }

  .service { left: 540px; width: 330px; }
  .service-breast { top: 312px; }
  .service-body { top: 550px; }
  .service-title { font-size: 22px; font-weight: 700; color: var(--ink); margin-bottom: 4px; }
  .service-list { list-style: none; margin-left: 20px; margin-bottom: 6px; }
  .service-list li {
    position: relative; padding-left: 22px;
    font-size: 17px; font-weight: 700; line-height: 1.35; color: var(--ink);
  }
  .service-list li::before {
    content: ""; position: absolute; left: 0; top: 5px;
    width: 12px; height: 12px; border-radius: 50%; background: var(--pink);
  }
  .service-copy { font-size: 17px; line-height: 1.4; color: var(--ink-soft); }

  .website {
    left: 615px; top: 812px;
    font-size: 20px; font-weight: 700; font-style: italic; color: var(--ink);
  }

  /* Award seal */
  .award-seal { left: 480px; top: 880px; }

  /* Location */
  .location { left: 690px; top: 915px; }
  .location-block {
    position: absolute; left: 20px; top: 6px; width: 150px;
    font-size: 15px; line-height: 1.3; color: var(--ink-soft); font-style: normal;
  }
  .location-city { font-weight: 700; color: var(--ink); letter-spacing: .5px; }
  .location-phone { font-weight: 700; color: var(--ink); }

  /* Footer menu */
  .footer-menu {
    left: 0; right: 0; top: 1124px; text-align: right; padding-right: 30px;
    font-size: 14px; font-weight: 700; color: var(--ink);
  }
  .footer-menu .dot { color: var(--pink); margin: 0 5px; }
</style>
</head>
<body>

  <div class="abs brand-name">Belleform</div>
  <div class="abs brand-tagline">Cosmetic Surgery and Medspa</div>

  <h1 class="abs headline">Perfect<br>Beach Body</h1>
  <svg class="abs headline-brace" width="380" height="50" viewBox="0 0 380 50" aria-hidden="true">
    <path d="M4 40 Q10 24 40 24 L170 24 Q188 24 194 6 Q200 24 218 24 L340 24 Q370 24 376 8"
          fill="none" stroke="var(--pink)" stroke-width="7" stroke-linecap="round"/>
  </svg>

  <div class="abs hero-photo" role="img" aria-label="Smiling woman in a dark bikini holding a colourful striped sarong at her hips, against a pale beach sky"></div>

  <svg class="abs divider-arrow" width="40" height="780" viewBox="0 0 40 780" aria-hidden="true">
    <line x1="20" y1="0" x2="20" y2="745" stroke="var(--pink)" stroke-width="12" stroke-dasharray="3 4"/>
    <path d="M6 738 L20 772 L34 738" fill="none" stroke="var(--pink)" stroke-width="4" stroke-linejoin="round"/>
  </svg>

  <div class="abs kicker">
    <span class="kicker-pink">Beautiful</span>
    <span class="kicker-dark">Breast</span>
    <span class="kicker-dark">Body</span>
  </div>
  <div class="abs kicker-amp">&amp;</div>

  <section class="abs service service-breast">
    <h2 class="service-title">Breast Procedures</h2>
    <ul class="service-list">
      <li>Breast Augmentation</li>
      <li>Breast Lift</li>
      <li>Breast Reduction</li>
    </ul>
    <p class="service-copy">The breast enhancement specialists at Belleform in Seaview, approach breast surgery with technical expertise and an artistic touch.</p>
  </section>

  <section class="abs service service-body">
    <h2 class="service-title">Body Procedures</h2>
    <ul class="service-list">
      <li>Mommy Makeover</li>
      <li>Tummy Tuck</li>
      <li>Liposuction</li>
      <li>Cellulite Treatment</li>
    </ul>
    <p class="service-copy">Our qualified Seaview plastic surgeons offer a variety of effective surgical &amp; non-surgical procedures to help you attain your ideal physique.</p>
  </section>

  <div class="abs website">www.belleform-clinic.com</div>

  <svg class="abs award-seal" width="200" height="200" viewBox="0 0 200 200" aria-hidden="true">
    <circle cx="100" cy="100" r="96" fill="var(--gold)"/>
    <circle cx="100" cy="100" r="70" fill="none" stroke="var(--gold-deep)" stroke-width="4"/>
    <circle cx="100" cy="100" r="50" fill="var(--gold-deep)" opacity=".35"/>
  </svg>

  <div class="abs location">
    <svg width="182" height="90" viewBox="0 0 182 90" aria-hidden="true">
      <path d="M14 4 Q4 4 4 14 L4 38 L0 45 L4 52 L4 76 Q4 86 14 86" fill="none" stroke="var(--pink)" stroke-width="2.5"/>
      <path d="M166 4 Q176 4 176 14 L176 38 L180 45 L176 52 L176 76 Q176 86 166 86" fill="none" stroke="var(--pink)" stroke-width="2.5"/>
    </svg>
    <address class="location-block">
      <div class="location-city">SEAVIEW</div>
      <div>1270 Harbor Lane</div>
      <div>Seaview, CA 90210</div>
      <div class="location-phone">(555) 014-2238</div>
    </address>
  </div>

  <nav class="abs footer-menu">
    Breast Procedures<span class="dot">•</span>Face Procedures<span class="dot">•</span>Body Procedures<span class="dot">•</span>For Men
  </nav>

</body>
</html>
```